KAZ Freightworks #ALLKAZ Business Cards & Letterhead

I am looking to business cards designed for our organization. We are currently undergoing a small re-branding that is taking place. Our organization is called KAZ Freightworks and we are headquartered in Phoenix, AZ. We primarily provide transportation and logistics services to the Meridel Parcel Bureau who is our largest customer. I would like to see a design that incorporates name, title, contact info, website, and address (this will be different depending on the employee). I would also like to see some color on the business card using our logo colors or a variation. I would like our logo on the back of the business card with the website displayed. The final design should communicate that we are a next generation transportation operate that focuses on being driver-first, customer-centric, innovative, and sustainable.We would also like our #ALLKAZ catch phrase incorporated as well.
Updates

Decision maker traveling outside of the country until Monday, November 25th.

Target Market(s)

Transportation & Logistics

Industry/Entity Type

Trucking Company

Contact Information for Business Card

-First and Last Name
-Position Title
-Contact Phone
-Contact Email
-Physical Address

Font styles to use
Serif

Colors

Designer to choose colors to be used in the design.

Requirements
Must have
• -KAZ logo prominently displayed
• -#ALLKAZ catch phrase used
• -Some amount of color, design gradient, etc.
• -Logo on the back with website listed (https://www.kazfreightco.example)

```html
<!DOCTYPE html>
<html lang="en">
<head>
<meta charset="utf-8">
<title>KAZ Freightworks Business Card</title>
<link href="https://fonts.googleapis.com/css2?family=Lato:wght@400;700;900&display=swap" rel="stylesheet">
<style>
  :root {
    --green: #80c342;
    --navy: #003a46;
    --white: #ffffff;
    --ink: #1f2a2e;
    --backdrop: #d9d9d9;
  }
  * { box-sizing: border-box; margin: 0; padding: 0; }
  html, body { width: 1200px; height: 802px; overflow: hidden; }
  body {
    position: relative;
    background: var(--backdrop);
    font-family: "Lato", Arial, sans-serif;
  }
  .card {
    position: absolute;
    top: 274px;
    width: 442px;
    height: 264px;
    overflow: hidden;
    box-shadow: 3px 4px 6px rgba(0,0,0,0.35);
  }
  .card-front { left: 136px; background: var(--white); }
  .card-back { left: 624px; background: var(--green); }

  .side-panel-top {
    position: absolute; left: 341px; top: 0; width: 101px; height: 129px;
    background: var(--green);
  }
  .side-panel-bottom {
    position: absolute; left: 341px; top: 129px; width: 101px; height: 135px;
    background: var(--navy);
  }
  .front-badge {
    position: absolute; left: 278px; top: 61px; width: 142px; height: 142px;
    border-radius: 50%; background: var(--white);
    display: flex; align-items: center; justify-content: center;
  }
  .front-badge-ring {
    width: 126px; height: 126px; border-radius: 50%;
    border: 4px solid var(--green);
    display: flex; align-items: center; justify-content: center;
  }
  .brand-name {
    font-weight: 900; color: var(--navy); font-size: 40px; letter-spacing: 1px; line-height: 1;
  }
  .person-name {
    position: absolute; left: 27px; top: 33px;
    font-weight: 900; font-size: 16px; color: var(--navy); letter-spacing: 0.2px;
  }
  .person-title {
    position: absolute; left: 27px; top: 51px; font-size: 12.5px; color: var(--ink);
  }
  .company-block {
    position: absolute; left: 27px; top: 124px; font-size: 12.5px; line-height: 16px; color: var(--ink);
  }
  .company-name { color: var(--green); font-weight: 700; }
  .contact-list {
    position: absolute; left: 27px; top: 188px; list-style: none;
    font-size: 12.5px; line-height: 16px; color: var(--ink);
  }
  .contact-list li { display: flex; align-items: center; gap: 2px; }
  .contact-icon { width: 14px; height: 14px; flex: none; }
  .hashtag {
    position: absolute; left: 358px; top: 230px; font-size: 12.5px; color: var(--green); letter-spacing: 0.3px;
  }

  .back-badge {
    position: absolute; left: 94px; top: 10px; width: 248px; height: 248px;
    border-radius: 50%; background: var(--navy);
    display: flex; align-items: center; justify-content: center;
  }
  .back-badge .brand-name { color: var(--white); font-size: 92px; letter-spacing: 3px; }
</style>
</head>
<body>
  <section class="card card-front" aria-label="Business card front">
    <div class="side-panel-top"></div>
    <div class="side-panel-bottom"></div>
    <div class="front-badge">
      <div class="front-badge-ring"><span class="brand-name">KAZ</span></div>
    </div>

    <h1 class="person-name">DANA MERROW</h1>
    <p class="person-title">Managing Director</p>

    <address class="company-block" style="font-style:normal">
      <div class="company-name">KAZ Freightworks</div>
      <div>421, Address line here</div>
      <div>Country Name, 45452</div>
    </address>

    <ul class="contact-list">
      <li>
        <svg class="contact-icon" viewBox="0 0 14 14" aria-hidden="true">
          <circle cx="7" cy="7" r="6.2" fill="none" stroke="#80c342" stroke-width="1.3"/>
          <path d="M4 5.2 Q7 3.2 10 5.2 L9.2 6.4 L8.2 6 L8 5.3 Q7 5 6 5.3 L5.8 6 L4.8 6.4 Z M5 7 H9 L9.6 10 H4.4 Z" fill="#003a46"/>
        </svg>
        <span>044-555 018 240</span>
      </li>
      <li>
        <svg class="contact-icon" viewBox="0 0 14 14" aria-hidden="true">
          <circle cx="7" cy="7" r="6.2" fill="none" stroke="#80c342" stroke-width="1.3"/>
          <rect x="3.8" y="4.8" width="6.4" height="4.6" fill="#003a46"/>
          <path d="M3.8 4.8 L7 7.4 L10.2 4.8" fill="none" stroke="#fff" stroke-width="0.8"/>
        </svg>
        <span>info@kazfreightco.example</span>
      </li>
      <li>
        <svg class="contact-icon" viewBox="0 0 14 14" aria-hidden="true">
          <circle cx="7" cy="7" r="6.2" fill="none" stroke="#80c342" stroke-width="1.3"/>
          <circle cx="7" cy="7" r="3.6" fill="#003a46"/>
          <path d="M3.4 7 H10.6 M7 3.4 Q5 7 7 10.6 M7 3.4 Q9 7 7 10.6" fill="none" stroke="#fff" stroke-width="0.6"/>
        </svg>
        <span>www.kazfreightco.example</span>
      </li>
    </ul>

    <p class="hashtag">#ALLKAZ</p>
  </section>

  <section class="card card-back" aria-label="Business card back">
    <div class="back-badge"><span class="brand-name">KAZ</span></div>
  </section>
</body>
</html>
```